Two Wine Labels, One Red One White

We are looking to create a brand image for our wines. There are two requirements by law that we need, however beyond that, the creativity comes from the designer. Required are:
On The Red Label, Alcohol 14.1White Label Alcohol 12.5, The Size, 750ML
SO One label for the red wine with alcohol at 14.1 in a 750 ML Bottle, and one Label for white with alcohol at 12.5 in a 750 ML bottle.

Hi All:
I have some more clarity to assist in the design work.
The Brand Name of the wine is Velmaric for both the red and the white
The name should appear as Velmaric with the Brackets around phonetical as seen here
[vel-mah-reek] Both the word and the phonetical spelling should appear.
and can be seen on wordlorebin.example The Brand Name text can be black
Label should be very light grey, I am trying to capture a Stone grey or texture from stone, although, NOT Marble.
The Red Label, The word "Red" should be in red
The White Label, The word "White" should be in White, all the original remaining elements remain as originally posted.

I look forward to hearing from you for any additional questions.
Updates

Just added a logo Not really seeing what we are trying to achieve, maybe using the logo in the design may assist

Target Market(s)

Wine Aficionados

Requirements
Must have
• Details described in Project Description above, these are required by law. The Name of the Brand will be posted shortly. For the moment if you take the project, just place red on one label and white on the other.
Nice to have
• These two wines are from California (USA), so the Sierra Nevada Mountains could be an inspiration, to outline of California or coast line, a vineyard (of course), a vine...We are in silicon valley, so there is a map of silicon valley with the Bay and ocean, something from a map could work, or let your creativity flow and not use any of these concepts.
Should not have
• I do not not care for decorative fonts, however all else is open

```html
<!DOCTYPE html>
<html lang="en">
<head>
<meta charset="utf-8">
<title>White Wine Label</title>
<link rel="stylesheet" href="https://fonts.googleapis.com/css2?family=Tinos&display=swap">
<style>
  :root {
    --page: #ffffff;
    --label-stone: #d9dfca;
    --frame-ink: #3a2e12;
    --oval-rim: #6e6a3c;
    --wood-light: #c47a4e;
    --wood-mid: #b2502c;
    --wood-deep: #9a3a1d;
    --vine-gold: #d8a637;
    --ornament-tone: #6b5a30;
    --varietal: #6b0f4a;
    --text-ink: #111111;
  }
  * { margin: 0; padding: 0; box-sizing: border-box; }
  html, body {
    width: 1200px;
    height: 900px;
    overflow: hidden;
    background: var(--page);
  }
  .wine-label {
    position: relative;
    width: 1200px;
    height: 900px;
    font-family: "Tinos", "Times New Roman", serif;
  }
  .label-art {
    position: absolute;
    inset: 0;
  }
  .varietal-name {
    position: absolute;
    left: 403px;
    top: 590px;
    font-size: 104px;
    line-height: 1;
    font-weight: 400;
    color: var(--varietal);
    letter-spacing: 0;
    white-space: nowrap;
  }
  .alcohol {
    position: absolute;
    left: 165px;
    top: 731px;
    color: var(--text-ink);
  }
  .alcohol-value {
    display: block;
    font-size: 56px;
    line-height: 1;
  }
  .alcohol-caption {
    display: block;
    font-size: 30px;
    line-height: 1;
    margin-top: 6px;
    padding-left: 7px;
  }
  .volume {
    position: absolute;
    left: 780px;
    top: 731px;
    font-size: 56px;
    line-height: 1;
    color: var(--text-ink);
  }
</style>
</head>
<body>
<main class="wine-label">
  <svg class="label-art" width="1200" height="900" viewBox="0 0 1200 900">
    <defs>
      <linearGradient id="wood-tone" x1="0" y1="0" x2="0" y2="1">
        <stop offset="0" stop-color="var(--wood-light)"/>
        <stop offset="0.18" stop-color="var(--wood-mid)"/>
        <stop offset="0.32" stop-color="var(--wood-light)"/>
        <stop offset="0.5" stop-color="var(--wood-deep)"/>
        <stop offset="0.68" stop-color="var(--wood-light)"/>
        <stop offset="0.84" stop-color="var(--wood-mid)"/>
        <stop offset="1" stop-color="var(--wood-light)"/>
      </linearGradient>
      <radialGradient id="vine-glow" cx="0.42" cy="0.38" r="0.6">
        <stop offset="0" stop-color="var(--vine-gold)" stop-opacity="0.55"/>
        <stop offset="1" stop-color="var(--vine-gold)" stop-opacity="0"/>
      </radialGradient>
      <linearGradient id="ornament-tone" x1="0" y1="0" x2="1" y2="1">
        <stop offset="0" stop-color="var(--ornament-tone)" stop-opacity="0.55"/>
        <stop offset="1" stop-color="var(--ornament-tone)" stop-opacity="0.3"/>
      </linearGradient>
    </defs>

    <rect class="label-ground" x="14" y="14" width="1172" height="872" rx="72" fill="var(--label-stone)"/>
    <rect class="frame-outer" x="14" y="14" width="1172" height="872" rx="72" fill="none" stroke="var(--frame-ink)" stroke-width="5"/>
    <rect class="frame-inner" x="30" y="30" width="1140" height="840" rx="58" fill="none" stroke="var(--frame-ink)" stroke-width="3"/>

    <path class="corner-flourish" role="img" aria-label="Scrolled acanthus flourish in the upper left corner"
          d="M30 150 Q30 30 150 30 L590 30 Q560 60 470 62 L150 70 Q80 90 80 200 L78 370 L38 370 Z"
          fill="url(#ornament-tone)"/>
    <path class="corner-flourish" role="img" aria-label="Scrolled acanthus flourish in the lower right corner"
          d="M1170 750 Q1170 870 1050 870 L625 870 Q650 840 740 838 L1050 830 Q1120 810 1120 700 L1125 520 L1165 520 Z"
          fill="url(#ornament-tone)"/>

    <ellipse class="medallion-rim" cx="590" cy="318" rx="313" ry="207" fill="none" stroke="var(--oval-rim)" stroke-width="2"/>
    <g class="medallion-image" role="img" aria-label="Golden grapevine with clusters and leaves carved into red-stained wood">
      <ellipse cx="590" cy="318" rx="303" ry="197" fill="url(#wood-tone)"/>
      <ellipse cx="590" cy="318" rx="303" ry="197" fill="url(#vine-glow)"/>
    </g>
    <ellipse class="medallion-crest" role="img" aria-label="Small scroll ornament crowning the medallion"
             cx="595" cy="110" rx="45" ry="14" fill="url(#ornament-tone)"/>
    <ellipse class="medallion-crest" role="img" aria-label="Small scroll ornament beneath the medallion"
             cx="585" cy="520" rx="52" ry="13" fill="url(#ornament-tone)"/>
  </svg>

  <h1 class="varietal-name">WHITE</h1>

  <p class="alcohol">
    <span class="alcohol-value">12.5%</span>
    <span class="alcohol-caption">Alcohol</span>
  </p>

  <p class="volume">750ml</p>
</main>
</body>
</html>
```